Agricultural Consulting Website

Provide a modern yet business like website for my new Agriculture Consulting Business in Australia called FenTrove. Whilst we are based in Australia we are targetting both domestic and international markets (especially in Asia). We are targetting corporate, small business, government and farmer clients. The design should compliment our logo also sourced through pixel guild. The webiste should be easy for me to keep updated on a regular basis without the need to go back to the designer.

Industry/Entity Type

Business

Requirements
Must have
• clean crisp feel
• be modern yet business like
• be able to be updated by myself easily

```html
<!DOCTYPE html>
<html lang="en">
<head>
<meta charset="utf-8">
<title>FenTrove – Agricultural Consulting</title>
<link rel="stylesheet" href="https://fonts.googleapis.com/css2?family=Mulish:wght@300;400;700;800&family=Arimo:wght@400;700&family=Open+Sans:wght@400;600&display=swap">
<style>
:root{
  --page-green:#5f9a0b;
  --head-green:#5c9a10;
  --brown:#6a2c00;
  --brown-dark:#5a2a00;
  --link-red:#9b1f1f;
  --text:#222;
  --rule:#c9c9c9;
  --white:#fff;
}
*{margin:0;padding:0;box-sizing:border-box}
html,body{width:1200px;height:1094px;overflow:hidden}
body{background:var(--page-green);font-family:"Arimo",Arial,sans-serif;color:var(--text);position:relative}
.site{position:absolute;left:120px;top:0;width:960px;height:1094px;background:var(--white)}

/* header */
.hero{position:absolute;left:0;top:0;width:960px;height:250px;
  background:linear-gradient(100deg,#cfe6a4 0%,#b4d87e 45%,#9ccb63 100%);overflow:hidden}
.topbar{position:absolute;left:0;top:0;width:960px;height:46px;background:rgba(40,38,26,.88);z-index:2}
.main-nav{position:absolute;left:324px;top:0;width:616px;height:46px;display:flex;justify-content:space-between;align-items:center;
  font-family:"Mulish",sans-serif;font-size:13px;list-style:none;z-index:3}
.main-nav li{color:#d4d4c8}
.main-nav li.current{color:var(--white)}
.brand{position:absolute;left:20px;top:0;width:239px;height:90px;background:var(--white);z-index:4;
  box-shadow:0 2px 6px rgba(0,0,0,.25);display:flex;align-items:center;gap:12px;padding-left:20px}
.brand-mark{width:34px;height:34px;background:var(--brown);border-radius:4px}
.brand-name{font-family:"Mulish",sans-serif;font-weight:700;font-size:33px;color:var(--head-green)}
.hero-title{position:absolute;left:26px;top:112px;font-family:"Mulish",sans-serif;color:var(--brown-dark);line-height:1;z-index:1}
.hero-title .line-1{display:block;font-size:36px;font-weight:800}
.hero-title .line-2{display:block;font-size:43px;font-weight:300;margin-top:4px}
.hero-photos{position:absolute;left:446px;top:46px;width:514px;height:204px;
  background:linear-gradient(90deg,rgba(156,203,99,0) 0%,#8fbf55 25%,#c9a064 60%,#4f8a2a 100%)}

/* body */
.content{position:absolute;left:20px;top:250px;width:600px}
.sidebar{position:absolute;left:663px;top:250px;width:276px}
.divider{position:absolute;left:641px;top:281px;width:1px;height:738px;background:var(--rule)}
h2{font-family:"Mulish",sans-serif;font-weight:800;color:var(--head-green);font-size:20px;text-transform:uppercase;letter-spacing:.2px}
.lead{font-family:"Arimo",sans-serif;color:var(--brown);font-size:17px;line-height:21px}
.body-copy{font-size:12.5px;line-height:20.5px;text-align:justify;color:#222}
.read-more{font-family:"Mulish",sans-serif;font-weight:800;font-size:13.5px;color:var(--brown);text-transform:uppercase;display:block}

.welcome{position:absolute;left:0;top:30px;width:603px}
.welcome .lead{margin-top:18px}
.welcome-photo{position:absolute;left:0;top:130px;width:157px;height:149px;background:linear-gradient(180deg,#5e8f2a,#7eae42 50%,#4f7a22)}
.welcome-text{position:absolute;left:171px;top:128px;width:432px}
.welcome-text .read-more{margin-top:8px}

.column-block{position:absolute;left:0;width:301px}
.column-block .lead{margin-top:10px;font-size:16.5px}
.column-block .body-copy{margin-top:12px;font-size:12px;line-height:19.5px}
.column-block .read-more{margin-top:10px;font-size:11.5px}
.mission{top:317px}
.expertise{top:568px}
.block-rule{position:absolute;left:0;top:547px;width:301px;height:1px;background:var(--rule)}
.farmer-photo{position:absolute;left:367px;top:307px;width:229px;height:464px;
  background:linear-gradient(180deg,#f1ede2 0%,#dfe4ef 40%,#c4d0ea 100%)}

.news-group{position:absolute;left:0;width:276px}
.news-group h2{margin-bottom:16px}
.news-item{margin-bottom:17px;font-family:"Open Sans",sans-serif;border-bottom:1px solid var(--rule);padding-bottom:1px;width:276px}
.news-date{font-size:13.5px;color:var(--brown)}
.news-title{font-size:13px;color:var(--head-green);margin-top:2px}
.news-text{font-size:12px;line-height:17px;color:#333;margin-top:3px}
.news-more{font-size:13px;color:var(--link-red)}
.recent{top:30px}
.events{top:313px}
.social{position:absolute;left:0;top:596px}
.social-list{list-style:none;display:grid;grid-template-columns:repeat(2,110px);gap:10px 14px;margin-top:18px}
.social-list li{display:flex;align-items:center;gap:8px;font-family:"Mulish",sans-serif;font-weight:700;font-size:15px;color:var(--brown)}
.social-dot{width:24px;height:24px;border-radius:50%;background:var(--brown)}

/* footer */
.site-footer{position:absolute;left:0;top:1047px;width:960px;height:47px;background:var(--brown-dark);
  display:flex;align-items:center;justify-content:space-between;padding:0 14px 0 17px;font-family:"Mulish",sans-serif;font-size:13px;color:var(--white)}
.footer-nav{display:flex;gap:15px;list-style:none}
.footer-nav li.current{color:#e2c23a}
</style>
</head>
<body>
<div class="site">
  <header class="hero">
    <div class="topbar"></div>
    <ul class="main-nav">
      <li class="current">Home</li><li>About Us</li><li>Area of Expertise</li><li>Tours and Events</li><li>Focus</li><li>Gallery</li><li>Our Team</li><li>Contact Us</li>
    </ul>
    <div class="brand"><span class="brand-mark"></span><span class="brand-name">FenTrove</span></div>
    <h1 class="hero-title"><span class="line-1">Lorem ipsum dolor sit</span><span class="line-2">consectetur adipiscing</span></h1>
    <div class="hero-photos" role="img" aria-label="Photo collage of farmers with a crate of apples, leafy greens, golden wheat and kale"></div>
  </header>

  <div class="divider"></div>

  <main class="content">
    <section class="welcome">
      <h2>Welcome to Fen Trove</h2>
      <p class="lead">Lorem ipsum dolor sit amet consecteture adipicsing elit.Lorem ipsum dolor sit amet, consectetur adipiscing elit. Sed id tempus enim.</p>
    </section>
    <div class="welcome-photo" role="img" aria-label="Photo of green crop rows in a field"></div>
    <div class="welcome-text">
      <p class="body-copy">Nam quis ligula a nibh fermentum venenatis vitae nec neque. Etiam non felis mi. Quisque feugiat, lectus non feugiat consectetur, purus ipsum nisl, a sollicitudin risus arcu elementum risus. Sed feugiat mollis neque. Suspendisse potenti. Sed libero dui, consequat vel ultrices quis, faucibus iaculis nisi. Pellentesque sit amet eleifend augue. Fusce viverra nisl eu magna imperdiet euismod a vel tortor. Donec vulputate</p>
      <span class="read-more">Read More</span>
    </div>

    <section class="column-block mission">
      <h2>Our Mission</h2>
      <p class="lead">Lorem ipsum dolor sit amet consecteture adipicsing elit.Lorem ipsum dolor</p>
      <p class="body-copy">Nam quis ligula a nibh fermentum venenatis vitae nec neque. Etiam non felis mi. Quisque feugiat, lectus non feugiat consectetur, purus ipsum nisl, a sollicitudin risus arcu elementum risus. Sed feugiat mollis neque. Suspendisse potenti.</p>
      <span class="read-more">Read More</span>
    </section>
    <div class="block-rule"></div>
    <section class="column-block expertise">
      <h2>Area of Expertise</h2>
      <p class="lead">Lorem ipsum dolor sit amet consecteture adipicsing elit.Lorem ipsum dolor</p>
      <p class="body-copy">Nam quis ligula a nibh fermentum venenatis vitae nec neque. Etiam non felis mi. Quisque feugiat, lectus non feugiat consectetur, purus ipsum nisl, a sollicitudin risus arcu elementum</p>
      <span class="read-more">Read More</span>
    </section>
    <div class="farmer-photo" role="img" aria-label="Photo of a farmer in a straw hat and overalls holding a basket of fresh vegetables"></div>
  </main>

  <aside class="sidebar">
    <section class="news-group recent">
      <h2>Recent News</h2>
      <article class="news-item"><p class="news-date">Date: 15.04.2013</p><p class="news-title">Lorem ipsum dolor sit amet, consectetur</p><p class="news-text">Aliquam erat volutpat. Aliquam erat volutpat. Pellentesque et arcu lorem.</p><p class="news-more">Read More</p></article>
      <article class="news-item"><p class="news-date">Date: 15.04.2013</p><p class="news-title">Lorem ipsum dolor sit amet, consectetur</p><p class="news-text">Aliquam erat volutpat. Aliquam erat volutpat. Pellentesque et arcu lorem.</p><p class="news-more">Read More</p></article>
    </section>
    <section class="news-group events">
      <h2>Events</h2>
      <article class="news-item"><p class="news-date">Date: 15.04.2013</p><p class="news-title">Lorem ipsum dolor sit amet, consectetur</p><p class="news-text">Aliquam erat volutpat. Aliquam erat volutpat. Pellentesque et arcu lorem.</p><p class="news-more">Read More</p></article>
      <article class="news-item"><p class="news-date">Date: 15.04.2013</p><p class="news-title">Lorem ipsum dolor sit amet, consectetur</p><p class="news-text">Aliquam erat volutpat. Aliquam erat volutpat. Pellentesque et arcu lorem.</p><p class="news-more">Read More</p></article>
    </section>
    <section class="social">
      <h2>Social</h2>
      <ul class="social-list">
        <li><span class="social-dot"></span>Share</li>
        <li><span class="social-dot"></span>Post</li>
        <li><span class="social-dot"></span>Connect</li>
        <li><span class="social-dot"></span>Watch</li>
      </ul>
    </section>
  </aside>

  <footer class="site-footer">
    <ul class="footer-nav">
      <li class="current">Home</li><li>About Us</li><li>Area of Expertise</li><li>Tours and Events</li><li>Focus</li><li>Gallery</li><li>Our Team</li><li>Contact Us</li>
    </ul>
    <p class="copyright">© Copyright FenTrove 2013. All right reserved.</p>
  </footer>
</div>
</body>
</html>
```